Ebook/Booklet Cover: Neue Arbeitswelten
Tolles Miteinander, hat genau gefühlt und erkannt wo ich hin wollte. Und war sehr geduldig, da ich die letzten Informationen zum Buch jetzt erst mit großer Verspätung übermitteln konnte. Gerne jederzeit wieder!
Zielgruppe
Beratung und Training für kleine und mittlere Unternehmen im Bereich Arbeitnehmerschutz (Arbeitssicherheit), Stressprävention und Aufbau von alltagstauglichen Arbeitsabläufen/Strukturen.
In diesem Buchprojekt jetzt trete ich jedoch nicht primär als Unternehmen auf, sondern als Autorin.
Zielgruppe: Bis jetzt Führungskräfte, Geschäftsführer, Personalmanagement in Unternehmen.
Das soll auch so bleiben nur ist mein Plan in Zukunft auch Privatpersonen anzusprechen.
Inhalt des Ebooks:
Ratgeber, Impulsgeber und Informationsvermittler zu den Themen 'Hybrides Arbeiten', 'Arbeiten im Home Office', 'Digitales Arbeiten' .
Einzelne Themen sind jeweils in einem eigenen Ebook.
Titel ist noch in Arbeit. Es sollten jedoch 2 Zeilen sein.
Eines welches das Thema grob beschreibt - zB 'Perspektiven zur Arbeitswelt der Zukunft' (Das bleibt immer gleich) und darunter 'Hybrides Arbeiten' (Das ist bei jedem Thema dann extra)
Es geht inhaltlich darum, welche Folgen haben diese neuen Arbeitssituationen für Körper - Geist und Psyche und wie geht man im Idealfall damit um. Und wie bereiten wir uns für diese enormen Veränderungen in der ZUkunft optimal vor.
Mit dem Ziel, dass sich der Leser Tipps rauspickt die er selbst umsetzen kann zu Hause. Und vielleicht auch eine neue Perspektive in diese neue Arbeitswelt bekommt.
Und auch Unternehmer und Personalverantwortliche haben so einen Leitfaden für die Zukunft.
Man könnte sagen 'Hoch wissenschaftliche Inhalte + gesetzliche Vorgaben (Also teilweise komplizierte + trockene Inhalte) sollen niederschwellig, leicht lesbar und unterhaltsam präsentiert werden.
Aufgabenstellung
Ich mag Klares. Sauberes. Harmonisches. Ein Mix aus 'edel, niveauvoll, professionell' und 'sympathisch, fröhlich, stylisch'
Nichts Überladenes, keine Reizüberflutung.
Und es darf ein klein wenig darf 'Spiritualität' durchkommen - muss aber nicht.
Auf meiner Homepage sieht man eine Kugel zwischen 2 Händen. Diese passt zB sehr gut zu mir: Verbindend, harmonisch, klar, 'rund'.
Ich habe diese Velmora Bildarchiv Datei angefügt - muss aber nicht verwendet werden!
Weiter unten, wo der Regler zu verschieben ist um Vorstellungen einzugrenzen ist mir aufgefallen, dass dies gar nicht so einfach so beschreiben ist ;-). Wenn eine klare Struktur da ist (zB weißer Hintergrund), Farben harmonisch sind darf ein Teil gerne verspielt und bunt sein als Akzent. Aber eben nicht chaotisch überladen.
Vom Typ her bin ich eher 'HIN ZU statt WEG VON'. Ein Buchcover zum Thema 'Durch Entspannung weniger Stress' würde bei mir zB keinen Kopf zeigen der Blitze und Chaos um sich hat. Sondern ein Kopf der entspannte, bunte, fließende Gedanken hat.
Mei, ich hoffe Ihr Kreativen die das lest habt Eure Kristallkugel zum Gedankenlesen dabei,... ist gar nicht so einfach meine Vorstellung in Worte zu fassen :-).
Zur Preisgestaltung in dem Projekt: Ich bin (Wie viele von uns) finanziell recht gebeutelt durch die aktuelle Situation. Daher geht aktuell nur das Minibudget.
Ich plane hier aber Schritt für Schritt mehr zu machen (Als Autorin) in Zukunft und es ist absolut die Möglichkeit einer weiteren Zusammenarbeit vorhanden.
Liebe Grüße an Euch alle!!
Update:
zu viel schwarze Farbe ist nicht so meines ;-), - ich tendiere zu hellen Designs...

```html
<!DOCTYPE html>
<html lang="de">
<head>
<meta charset="utf-8">
<title>Perspektiven zur Arbeitswelt der Zukunft – Hybrides Arbeiten</title>
<link rel="stylesheet" href="https://fonts.googleapis.com/css2?family=Nunito+Sans:wght@300;400;700;800;900&display=swap">
<style>
  :root {
    --backdrop: #bbbbbb;
    --paper: #ffffff;
    --navy: #1f2e42;
    --slate: #8e969f;
    --frame-outer: #e2e3e6;
    --frame-inner: #c9ccd2;
    --photo-deep: #1c2c44;
    --photo-mid: #34476a;
  }
  html, body {
    margin: 0;
    width: 1200px;
    height: 1200px;
    overflow: hidden;
    background: var(--backdrop);
    font-family: "Nunito Sans", sans-serif;
  }
  .cover {
    position: absolute;
    left: 290px;
    top: 118px;
    width: 620px;
    height: 958px;
    background: var(--paper);
    color: var(--navy);
  }
  .series {
    position: absolute;
    left: 63px;
    top: 44px;
    width: 494px;
    display: flex;
    align-items: center;
    gap: 10px;
  }
  .series-rule { flex: 1; height: 1px; background: var(--slate); }
  .series-label {
    font-weight: 900;
    font-size: 18px;
    letter-spacing: 8.5px;
    color: var(--slate);
    margin-right: -8.5px;
    white-space: nowrap;
  }
  .title {
    position: absolute;
    left: 63px;
    top: 108px;
    width: 494px;
    text-align: center;
    margin: 0;
    white-space: nowrap;
  }
  .title-main {
    display: block;
    font-weight: 800;
    font-size: 65px;
    line-height: 1;
    letter-spacing: -1px;
  }
  .title-sub {
    display: block;
    font-weight: 300;
    font-size: 26px;
    line-height: 1.2;
    letter-spacing: 0.9px;
    margin-top: 4px;
  }
  .visual {
    position: absolute;
    left: 63px;
    top: 226px;
    width: 494px;
    height: 494px;
    background: var(--frame-outer);
  }
  .visual-inner {
    position: absolute;
    left: 36px; top: 36px;
    width: 422px; height: 422px;
    background: var(--frame-inner);
  }
  .visual-photo {
    position: absolute;
    left: 31px; top: 31px;
    width: 360px; height: 360px;
    background: radial-gradient(circle at 50% 48%, var(--photo-mid) 0%, var(--photo-deep) 65%);
  }
  .audience {
    position: absolute;
    left: 40px;
    top: 741px;
    width: 540px;
    text-align: center;
  }
  .audience-lead {
    margin: 0;
    font-weight: 800;
    font-size: 14.5px;
    line-height: 20px;
    letter-spacing: 0.6px;
  }
  .audience-detail {
    margin: 2px 0 0;
    font-weight: 400;
    font-size: 12.5px;
    line-height: 20px;
    letter-spacing: 0.5px;
  }
  .author {
    position: absolute;
    left: 0; top: 884px;
    width: 620px;
    text-align: center;
    font-size: 11px;
    line-height: 13px;
    letter-spacing: 4px;
    color: var(--slate);
  }
</style>
</head>
<body>
  <main class="cover">
    <div class="series">
      <span class="series-rule"></span>
      <span class="series-label">HYBRIDES ARBEITEN</span>
      <span class="series-rule"></span>
    </div>
    <h1 class="title">
      <span class="title-main">PERSPEKTIVEN</span>
      <span class="title-sub">ZUR ARBEITSWELT DER ZUKUNFT</span>
    </h1>
    <div class="visual">
      <div class="visual-inner">
        <div class="visual-photo" role="img" aria-label="Foto: zwei Hände umschließen eine leuchtende Netzwerkkugel vor dunkelblauem Anzug"></div>
      </div>
    </div>
    <section class="audience">
      <p class="audience-lead">BERATUNG UND TRAINING<br>FÜR KLEINE UND MITTLERE UNTERNEHMEN</p>
      <p class="audience-detail">IM BEREICH ARBEITNEHMERSCHUTZ (ARBEITSSICHERHEIT),<br>STRESSPRÄVENTION UND AUFBAU VON ALLTAGSTAUGLICHEN<br>ARBEITSABLÄUFEN/STRUKTUREN.</p>
    </section>
    <div class="author">AUTOR<br>NAME</div>
  </main>
</body>
</html>
```